Website Redesign Project

Bright Harbor Planning provides project management and project controls consultancy services to companies in many industry sectors, within Australia and overseas. My company has been developing a business brand through forging strong business relationships within industry. We provide innovative tools, concepts and solutions to management teams to assist them in better plan and managing there project portfolios.
SECTORS OF INDUSTRY WE SERVICE
★Oil & Gas
★Minerals & Metals
★Petrochemical
★Manufacturing
★Building & Construction
★Telecommunications
★Rail
★Civil
OLD WEBSITE
My old website www.brightharborplanning.com.au needs a complete overhaul in terms of how the web pages look and feel. I am trying to get away from the grey, washed out look as it is uninviting and dull. My clients commented that my webpage does not reflect who I am as a company or my core values. Think total redesign
DESIGN
I would like a webpage design that is modern and has a corporate image. It must be elegant, classy, and have an overall glossy appearance. I want something exciting that creates some excellent feedback from clients. It needs to have a savvy appearance and an attitude of a market leader. A generic website template cannot be used as I provide a unique service to clients. I do not need a website design that looks like my compeditors, I want something that stands out in the crowd and effectivly markets my bussinesses brand. I want my website to represent quality, so only high resolution images that are clear, sharp and in focus can be used. With this design, throw your standard webpage design concepts out the window, as I want something fresh, innovative, exciting and inviting. The overall design should appear uncluttered as all content needs to be there for a reason, so think functional.
It must be professional and of the highest calibre as my clients expect nothing less. I provide clients with innovative tools, concepts and solutions, so the design needs to be edgy and creative to align with my company’s core business services. The new design must promote the company’s brand and us as a market leader. It must communicate that we service many industry sectors and reflect our company’s creativity, vision, energy and drive.
WEBPAGE WRITTEN CONTENT
I am happy with the written content on each page within my old website. You may arrange the text how you see fit within the new design. On the main page of my old website the text is under scored, I am not a big fan of this. I currently do not like the format the text is in, I am looking for a formatt that is easy to read, looks flattering and pleasing to the eye.
MAIN PAGE DESIGN
The main page design needs to focus on my company as a brand, it must promote that I service many industry sectors. My old webpage had me pigeon holed as only providing services to oil and gas. This is incorrect as I service oil & gas, metals and minerals, Petrochemical, Manufacturing, Building & Construction, Telecommunications, Rail and civil.
WEBPAGE COLUR PREFERENCE
Prefer a white background with plenty of colour
TESTIMONIAL TAB
The testimonial tab on the task bar can be removed as it is no longer required.
FINISHED PRODUCT
The finished product will be uploaded by you to a nominated web hosting account. I will need a copy of all files associated with the design. A copy of the finished product will also be provided in formats that can me imported to Xara Pro Designer as I will update my website in 6 months or so using this tool.
Updates
I have updated the design brief after recieving feedback from several designers
Thanks
Reason: Some designers have asked for more time
Hi All
I have just launched another project called "bright harbor planning business card redesign project", you are all welcome to join this project.
Thanks
Target Market(s)
★Oil and Gas
★Mining and Resources
★Building and infrastructure
★Petrochemical
★Civil and roads
★Rail
Industry/Entity Type
Industry
Requirements
Must have
- ★Draw you in
★Hold your attention
★Identify company brand
★Highlight skills experience and expertise
★Be a unique design not generic
Should not have
- ★The webpage design should not be old fashioned
★ The design should not be based off a generic design template
★The webpage should not be cluttered; everything needs to be there for a reason.

```html
<!DOCTYPE html>
<html lang="en">
<head>
<meta charset="utf-8">
<title>Bright Harbor Planning</title>
<link rel="stylesheet" href="https://fonts.googleapis.com/css2?family=Ubuntu:wght@300;400;500;700&display=swap">
<style>
:root{
  --white:#ffffff;
  --ink:#1d1d1d;
  --nav:#3a4e6a;
  --body:#3c3c3c;
  --red:#a52a0a;
  --orange:#e8901a;
  --bullet:#d8251d;
  --footer:#000000;
  --footer-text:#9a9a9a;
  --caption-bg:rgba(30,36,62,.78);
}
*{margin:0;padding:0;box-sizing:border-box}
html,body{width:1200px;height:948px;overflow:hidden;background:var(--white)}
body{position:relative;font-family:'Ubuntu',sans-serif;color:var(--ink)}
.abs{position:absolute}

.brand{left:146px;top:40px;display:flex;align-items:center;gap:10px}
.brand-dot{width:40px;height:40px;border-radius:50%;background:var(--red)}
.brand-name{font-size:24px;font-weight:700;color:var(--red);line-height:1}
.brand-tag{left:196px;top:72px;font-size:6.5px;color:var(--ink)}

.social{top:55px;width:26px;height:26px;border-radius:50%}
.s1{left:876px;background:#3b5a9a}
.s2{left:918px;background:#eb9a2a}
.s3{left:962px;background:#c8261f}
.s4{left:1002px;background:#4a86c2}

.nav{top:104px;left:0;width:1200px;height:22px;font-size:15.5px;color:var(--nav);font-weight:400}
.nav span{position:absolute;top:0}

.hero{left:0;top:133px;width:1200px;height:373px;
  background:linear-gradient(90deg,#8d8d8d 0%,#5a5a5c 25%,#3c3d42 45%,#4b4b50 60%,#c9c3b6 72%,#e7892a 82%,#f39a35 92%,#c26a1e 100%)}
.caption{left:151px;top:295px;width:487px;height:136px;background:var(--caption-bg)}
.caption h1{position:absolute;left:29px;top:12px;font-size:33px;font-weight:400;color:var(--white);white-space:nowrap}
.caption p{position:absolute;left:29px;top:60px;width:456px;font-size:14.8px;line-height:17.6px;color:var(--white)}
.btn{display:flex;align-items:center;justify-content:center;border-radius:17px;color:var(--white);font-family:Arial,Helvetica,sans-serif;font-size:15.5px}
.btn-vision{left:472px;top:415px;width:142px;height:33px;background:var(--red)}
.arrows{left:998px;top:462px}

.h2{font-size:28px;font-weight:400;color:var(--ink)}
.news-title{left:148px;top:546px}
.thumb{left:148px;top:597px;width:97px;height:72px;background:linear-gradient(135deg,#c8822a,#4a5a78 55%,#d9a040)}
.news-head{left:258px;top:596px;width:380px;font-size:15.5px;font-weight:500;line-height:17px}
.news-body{left:258px;top:640px;width:350px;font-size:12.5px;font-weight:300;line-height:16.6px;color:var(--body)}
.btn-more{left:258px;top:727px;width:108px;height:34px;background:var(--orange)}
.btn-all{left:375px;top:727px;width:95px;height:34px;background:var(--red)}

.proj-title{left:692px;top:548px}
.sectors{list-style:none;font-size:11.8px;line-height:16.6px;color:var(--ink)}
.sectors li{position:relative;padding-left:12px;white-space:nowrap}
.sectors li::before{content:"";position:absolute;left:1px;top:6px;width:4px;height:4px;border-radius:50%;background:var(--bullet)}
.col1{left:694px;top:596px}
.col2{left:823px;top:596px}

.help-icon{left:695px;top:722px}
.help-title{left:754px;top:718px;font-size:28px;font-weight:400;line-height:1}
.help-sub{left:754px;top:751px;font-size:13px;font-weight:300}

.footer{left:0;top:797px;width:1200px;height:151px;background:var(--footer)}
.copy{left:375px;top:861px;font-size:11px;line-height:14.8px;color:var(--footer-text)}
.fcol{top:836px;font-size:10.4px;line-height:14.8px;color:var(--footer-text)}
.fcol h3{font-size:10.4px;font-weight:500;color:var(--white);margin-left:-10px;margin-bottom:0}
.f1{left:666px}.f2{left:781px}.f3{left:947px}
</style>
</head>
<body>
<header>
  <div class="abs brand"><div class="brand-dot"></div><div class="brand-name">Bright Harbor Planning</div></div>
  <div class="abs brand-tag">Providing Effective Project Controls and Management Solutions</div>
  <div class="abs social s1" aria-label="Social link"></div>
  <div class="abs social s2" aria-label="Feed link"></div>
  <div class="abs social s3" aria-label="Video link"></div>
  <div class="abs social s4" aria-label="Blog link"></div>
  <nav class="abs nav">
    <span style="left:162px">About Us</span>
    <span style="left:287px">Expertise</span>
    <span style="left:403px">Knowledge</span>
    <span style="left:520px">Experience</span>
    <span style="left:642px">Projects</span>
    <span style="left:743px">Focus</span>
    <span style="left:837px">Contact</span>
    <span style="left:935px">Recruitment</span>
  </nav>
</header>

<section class="abs hero" role="img" aria-label="Gloved hand holding lumps of coal"></section>
<div class="abs caption">
  <h1>Bright Harbor Planning</h1>
  <p>I provide services to companies in the mining and oil and gas sector, to enabling them to plan and manage their construction projects more effectively.</p>
</div>
<div class="abs btn btn-vision">Read Our Vision</div>
<svg class="abs arrows" width="40" height="26" viewBox="0 0 40 26">
  <polyline points="12,3 4,13 12,23" fill="none" stroke="#fff" stroke-width="3"/>
  <polyline points="28,3 36,13 28,23" fill="none" stroke="#fff" stroke-width="3"/>
</svg>

<h2 class="abs h2 news-title">Latest News</h2>
<div class="abs thumb" role="img" aria-label="Close-up of electronic components"></div>
<div class="abs news-head">Exceed client’s expectations Act with integrity and honesty</div>
<p class="abs news-body">I have 20 years industry experience within engineering, construction, mining and the oil &amp; gas sector. I am well equipped to assist you and your company to deliver successful project outcomes..</p>
<div class="abs btn btn-more">Read More</div>
<div class="abs btn btn-all">All News</div>

<h2 class="abs h2 proj-title">Projects</h2>
<ul class="abs sectors col1">
  <li>Oil &amp; Gas</li><li>Iron Ore</li><li>Coal</li><li>Civil</li><li>Tenders</li><li>Telecomunications</li>
</ul>
<ul class="abs sectors col2">
  <li>New Industry</li><li>Petrochemical</li><li>Building And Constructionoil &amp; Gas</li><li>Engineering</li><li>Manufacturing</li><li>Rail</li>
</ul>
<svg class="abs help-icon" width="46" height="46" viewBox="0 0 46 46">
  <circle cx="23" cy="23" r="22" fill="#111"/>
  <rect x="12" y="15" width="22" height="16" rx="2" fill="#fff"/>
  <polyline points="12,16 23,25 34,16" fill="none" stroke="#111" stroke-width="2.5"/>
</svg>
<div class="abs help-title">Need Help .</div>
<div class="abs help-sub">Contact us now</div>

<footer class="abs footer"></footer>
<div class="abs copy">©Copyright by 2013 Bright Harbor Planning.<br>All rights reserved</div>
<div class="abs fcol f1"><h3>SOFTWARE</h3>Advice<br>Vision<br>Solutions<br>Solutions<br>Perspective</div>
<div class="abs fcol f2"><h3>CONTACTS</h3>Develop and evolve<br>Streamlines processes<br>Embrace and drive change<br>outcomes</div>
<div class="abs fcol f3"><h3>RESOURCES</h3>Systems<br>Standards<br>Procedures<br>Process</div>
</body>
</html>
```